corrigan mechanical repairs and welding

vehicle servicing
diesel repairs
motor rebuilds
tractor repairs
all types of welding

Industry/Entity Type

Welding

Contact Information for Business Card

RHYS MOTTRAM
0417395826

Font styles to use
Serif

Colors

Designer to choose colors to be used in the design.

```html
<!DOCTYPE html>
<html lang="en">
<head>
<meta charset="utf-8">
<title>Mechanical Repairs Welding — Business Card</title>
<link rel="stylesheet" href="https://fonts.googleapis.com/css2?family=Crimson+Pro:wght@400;600;700&display=swap">
<style>
  :root {
    --backdrop: #5c5d60;
    --card-cream: #fbf9ea;
    --title-maroon: #7a1f2c;
    --name-coral: #ec5e5e;
    --rule-coral: #ef5a5c;
    --rule-peach: #f6cfa4;
    --band-brown: #3a1d19;
    --band-text: #fbf3e6;
  }
  * { margin: 0; padding: 0; box-sizing: border-box; }
  html, body {
    width: 1200px;
    height: 724px;
    overflow: hidden;
    background: var(--backdrop);
    font-family: "Crimson Pro", Georgia, serif;
  }
  .stage {
    position: relative;
    width: 1200px;
    height: 724px;
    display: flex;
    align-items: center;
    justify-content: center;
  }
  .business-card {
    position: relative;
    width: 840px;
    height: 480px;
    background: var(--card-cream);
    overflow: hidden;
    box-shadow: 0 10px 30px rgba(0,0,0,0.35);
  }
  .card-title {
    position: absolute;
    top: 52px;
    left: 0;
    width: 100%;
    text-align: center;
    color: var(--title-maroon);
    font-weight: 700;
    font-size: 56px;
    line-height: 1.0;
    letter-spacing: 2px;
    text-transform: uppercase;
  }
  .card-name {
    position: absolute;
    top: 214px;
    left: 0;
    width: 100%;
    text-align: center;
    color: var(--name-coral);
    font-weight: 400;
    font-size: 38px;
    letter-spacing: 1.5px;
    text-transform: uppercase;
  }
  .rule-coral {
    position: absolute;
    top: 296px;
    left: 0;
    width: 100%;
    height: 7px;
    background: var(--rule-coral);
  }
  .rule-peach {
    position: absolute;
    top: 303px;
    left: 0;
    width: 100%;
    height: 6px;
    background: var(--rule-peach);
  }
  .services-band {
    position: absolute;
    top: 309px;
    left: 0;
    width: 100%;
    height: 171px;
    background: var(--band-brown);
    color: var(--band-text);
    font-size: 25px;
    letter-spacing: 1px;
    text-transform: uppercase;
  }
  .service { position: absolute; white-space: nowrap; line-height: 1; }
  .service--servicing { left: 42px; top: 28px; }
  .service--diesel { left: 62px; top: 58px; }
  .service--tractor { right: 44px; top: 74px; }
  .service--motor { right: 44px; top: 104px; }
  .service--welding { left: 0; width: 100%; text-align: center; top: 132px; }
</style>
</head>
<body>
  <main class="stage">
    <section class="business-card" aria-label="Business card">
      <h1 class="card-title">Mechanical Repairs<br>Welding</h1>
      <p class="card-name">Your Name Here</p>
      <div class="rule-coral"></div>
      <div class="rule-peach"></div>
      <ul class="services-band" style="list-style:none">
        <li class="service service--servicing">Vehicle Servicing</li>
        <li class="service service--diesel">Diesel Repairs</li>
        <li class="service service--tractor">Tractor Repairs</li>
        <li class="service service--motor">Motor Rebuilds</li>
        <li class="service service--welding">All Types of Welding</li>
      </ul>
    </section>
  </main>
</body>
</html>
```